Ridgeway Patrol Website Design

Hello Designers. I am an agency and am helping a security company get a better look. I have a new logo and a car done up. We are looking for a fresh look using the blue and the gold. Open to a complimentary color.

Here is the old site
https://moravanguard.com/

Here is another design for photos and everything. We weren't sold on it because we wanted to make it simple like the first one.

https://ww2.moravanguard.com/

Attached is also the copy I would like to put on there.

I am looking for tough, competent and simple. Our customers are contruction companies, event planners etc. It has to be clean and easy.

One thing we can't provide yet is photos. We are anticipating photos of our team with arms folded beside the car, close up of the owner with a logo'd shirt on. Pictures of an Ridgeway Patrol job site etc. (which most of the time is construction. They also do Mall security. You can see if you want to use stock photos for now.

I wanted to get the look of the front page done first. Hoping for something really awesome. Have fun.

```html
<!DOCTYPE html>
<html lang="en">
<head>
<meta charset="utf-8">
<title>Ridgeway Patrol — Security Professional</title>
<link href="https://fonts.googleapis.com/css2?family=Bebas+Neue&family=Poppins:wght@400;500;600&family=Roboto+Slab:wght@500&display=swap" rel="stylesheet">
<style>
:root{
  --gold:#9c6a00;
  --gold-soft:#a8781a;
  --blue:#0d3466;
  --cream:#f3ece1;
  --ink:#111;
  --muted:#777;
  --line:#e2e2e2;
  --white:#fff;
}
*{margin:0;padding:0;box-sizing:border-box}
html,body{width:1200px;height:3472px;overflow:hidden}
body{position:relative;font-family:"Poppins",sans-serif;color:var(--ink);background:var(--white)}
.abs{position:absolute}
.brand{font-family:"Poppins",sans-serif;font-weight:600;color:var(--white);font-size:20px;line-height:1.1;text-align:center;display:flex;flex-direction:column;align-items:center;gap:8px}
.brand-mark{width:14px;height:14px;background:var(--white)}
.btn{position:absolute;background:var(--gold);color:var(--white);font-size:12px;font-weight:600;text-transform:uppercase;display:flex;align-items:center;justify-content:center;letter-spacing:.2px}
.btn::after{content:"";position:absolute;right:0;bottom:0;border-style:solid;border-width:0 0 22px 22px;border-color:transparent transparent var(--white) transparent}
.btn.blue-corner::after{border-color:transparent transparent var(--blue) transparent}
.nav{top:22px;left:448px;display:flex;gap:0;font-size:11px;color:var(--white);text-transform:uppercase}
.nav span{position:absolute;white-space:nowrap}
.hero-title{left:60px;top:188px;font-family:"Bebas Neue",sans-serif;color:var(--white);font-size:86px;line-height:90px;letter-spacing:1px}
.hero-sub{left:60px;top:396px;font-family:"Roboto Slab",serif;color:var(--white);font-size:14px}
.sec-title{font-family:"Poppins",sans-serif;font-weight:500;font-size:31px;text-transform:uppercase;letter-spacing:-.3px;white-space:nowrap}
.card{position:absolute;top:788px;width:263px;height:307px;border:1px solid var(--line);background:var(--white);text-align:center}
.card .ph{position:absolute;left:0;top:0;width:263px;height:180px}
.badge{position:absolute;left:50%;transform:translateX(-50%)}
.card h3{position:absolute;top:208px;width:100%;font-size:14px;font-weight:500}
.card p{position:absolute;top:232px;left:14px;right:14px;font-size:12px;line-height:20px;color:var(--muted)}
.dots{left:580px;top:1110px;display:flex;gap:8px}
.dots i{width:7px;height:7px;background:#d8cbb0;display:block}
.dots i.on{background:var(--blue)}
.about-text{left:563px;top:1363px;width:400px;color:var(--white);font-size:12px;line-height:19.5px}
.stat{color:var(--white);font-size:14px;font-weight:500;line-height:22px}
.ind{position:absolute;width:189px;height:188px;background:var(--white);box-shadow:0 0 12px rgba(0,0,0,.1);text-align:center}
.ind h4{position:absolute;top:106px;width:100%;font-size:14px;font-weight:500}
.ind p{position:absolute;top:128px;left:14px;right:14px;font-size:12px;line-height:20px;color:var(--muted)}
.body-text{font-size:12px;line-height:19.5px;color:#222}
.foot-h{color:var(--white);font-size:15px;font-weight:500}
.foot-list{list-style:none;color:var(--white);font-size:12px;line-height:22.5px}
.foot-list li{position:relative;padding-left:22px}
.foot-list li::before{content:"";position:absolute;left:0;top:8px;width:6px;height:6px;border:1px solid var(--white);border-radius:50%}
.contact-row{display:flex;align-items:center;gap:14px;color:var(--white);font-size:12px;line-height:17px}
.copy{left:0;top:3445px;width:1200px;height:27px;background:var(--blue);color:var(--white);font-size:12px;display:flex;align-items:center;justify-content:center}
</style>
</head>
<body>

<!-- HERO -->
<svg class="abs" style="left:0;top:0" width="1200" height="640" viewBox="0 0 1200 640">
  <defs>
    <linearGradient id="heroPh" x1="0" y1="0" x2="1" y2="1">
      <stop offset="0" stop-color="#5a5046"/><stop offset=".55" stop-color="#2d2a28"/><stop offset="1" stop-color="#1a1a1c"/>
    </linearGradient>
  </defs>
  <rect width="1200" height="637" fill="url(#heroPh)" role="img" aria-label="Photo of a security guard in a dark suit speaking into a radio"/>
  <polygon points="0,0 478,0 590,580 0,636" fill="#9c6a00" opacity=".9"/>
  <polygon points="478,0 494,0 728,640 0,640 0,634 590,580" fill="#f3ece1"/>
</svg>

<div class="abs brand" style="left:40px;top:38px;width:160px"><span class="brand-mark"></span>Ridgeway Patrol</div>

<nav class="abs nav" aria-label="Main">
  <span style="left:0">Home</span>
  <span style="left:67px">Security Services</span>
  <span style="left:209px">Industries</span>
  <span style="left:314px">Training</span>
  <span style="left:404px">Careers</span>
  <span style="left:494px">About Us</span>
</nav>
<div class="btn" style="left:1024px;top:11px;width:116px;height:37px">Contact Us</div>

<h1 class="abs hero-title">Security<br>Professional</h1>
<p class="abs hero-sub">Security For New Brunswick Businesses &amp; Events</p>
<div class="btn" style="left:60px;top:428px;width:116px;height:36px">Contact Us</div>

<!-- SECURITY SERVICE -->
<h2 class="abs sec-title" style="left:455px;top:712px">Security Service</h2>

<div class="card" style="left:168px">
  <div class="ph" style="background:linear-gradient(135deg,#6f7f95,#1d2430)" role="img" aria-label="Photo of a guard on stationary patrol in a stairwell"></div>
  <svg class="abs" style="left:0;top:160px" width="263" height="22"><polygon points="0,22 263,0 263,22" fill="#fff"/></svg>
  <svg class="badge" style="top:148px" width="56" height="64" viewBox="0 0 56 64"><polygon points="28,0 56,12 56,40 28,64 0,40 0,12" fill="#9c6a00"/><circle cx="28" cy="30" r="10" fill="none" stroke="#fff" stroke-width="2"/></svg>
  <h3>Static Security</h3>
  <p>We provide stationary and foot patrol for retail spaces and ensure our uniformed security</p>
</div>
<div class="card" style="left:461px">
  <div class="ph" style="background:linear-gradient(135deg,#dfe6ee,#3b4452)" role="img" aria-label="Photo of a team of officers gathered in an office"></div>
  <svg class="abs" style="left:0;top:160px" width="263" height="22"><polygon points="0,22 263,0 263,22" fill="#fff"/></svg>
  <svg class="badge" style="top:148px" width="56" height="64" viewBox="0 0 56 64"><polygon points="28,0 56,12 56,40 28,64 0,40 0,12" fill="#9c6a00"/><circle cx="26" cy="28" r="8" fill="none" stroke="#fff" stroke-width="2"/><line x1="32" y1="34" x2="38" y2="40" stroke="#fff" stroke-width="2"/></svg>
  <h3>Investigations</h3>
  <p>Whatever your investigative needs are give us a call we would be glad to help.</p>
</div>
<div class="card" style="left:754px">
  <div class="ph" style="background:linear-gradient(135deg,#c9c3c8,#1f1f24)" role="img" aria-label="Photo of a uniformed guard with a radio in a retail store"></div>
  <svg class="abs" style="left:0;top:160px" width="263" height="22"><polygon points="0,22 263,0 263,22" fill="#fff"/></svg>
  <svg class="badge" style="top:148px" width="56" height="64" viewBox="0 0 56 64"><polygon points="28,0 56,12 56,40 28,64 0,40 0,12" fill="#9c6a00"/><rect x="20" y="22" width="16" height="16" fill="none" stroke="#fff" stroke-width="2"/></svg>
  <h3>Retail Security</h3>
  <p>Retail Security We provide stationary and foot patrol for retail spaces and ensure our</p>
</div>
<div class="abs dots"><i></i><i class="on"></i><i></i></div>

<!-- ABOUT -->
<svg class="abs" style="left:0;top:1205px" width="1200" height="420" viewBox="0 0 1200 420">
  <polygon points="0,0 1200,0 1200,358 310,406 0,420" fill="#9c6a00"/>
  <polygon points="310,406 1200,358 1200,364 310,412" fill="#0d3466"/>
</svg>
<svg class="abs" style="left:0;top:1283px" width="392" height="490" viewBox="0 0 392 490">
  <defs><linearGradient id="aboutPh" x1="0" y1="0" x2="1" y2="1"><stop offset="0" stop-color="#3f6a94"/><stop offset="1" stop-color="#0d3466"/></linearGradient></defs>
  <polygon points="0,40 150,0 392,70 360,300 150,490 0,380" fill="url(#aboutPh)" role="img" aria-label="Photo of a security officer in a suit with an earpiece, tinted blue"/>
</svg>
<h2 class="abs sec-title" style="left:563px;top:1303px;color:var(--white)">About Us</h2>
<p class="abs about-text">We can meet any security need. Ridgeway Patrol is located in Moncton, New Brunswick serving all of New Brunswick. We offer complete security services including event security, uniformed security and personal security services.</p>
<svg class="abs" style="left:562px;top:1462px" width="58" height="60" viewBox="0 0 58 60"><polygon points="29,0 58,10 58,36 29,60 0,36 0,10" fill="#fff"/><text x="29" y="32" text-anchor="middle" font-family="Poppins,sans-serif" font-weight="600" font-size="14" fill="#0d3466">200+</text></svg>
<div class="abs stat" style="left:636px;top:1468px">Security<br>Professionals</div>
<svg class="abs" style="left:758px;top:1462px" width="58" height="60" viewBox="0 0 58 60"><polygon points="29,0 58,10 58,36 29,60 0,36 0,10" fill="#fff"/><text x="29" y="32" text-anchor="middle" font-family="Poppins,sans-serif" font-weight="600" font-size="14" fill="#0d3466">24</text></svg>
<div class="abs stat" style="left:831px;top:1468px">Security<br>Experience</div>

<!-- INDUSTRIES -->
<h2 class="abs sec-title" style="left:527px;top:1714px">Industries Served</h2>

<div class="ind" style="left:62px;top:1845px"><svg class="abs" style="left:64px;top:18px" width="60" height="76" viewBox="0 0 60 76"><polygon points="30,2 58,14 58,44 30,74 2,44 2,14" fill="none" stroke="#0d3466" stroke-width="5"/><rect x="20" y="26" width="20" height="18" fill="none" stroke="#9c6a00" stroke-width="2"/></svg><h4>Construction</h4><p>Lorem ipsum is dummy printing text industry.</p></div>
<div class="ind" style="left:280px;top:1798px"><svg class="abs" style="left:64px;top:10px" width="60" height="76" viewBox="0 0 60 76"><polygon points="30,2 58,14 58,44 30,74 2,44 2,14" fill="none" stroke="#9c6a00" stroke-width="5"/><circle cx="30" cy="36" r="10" fill="none" stroke="#0d3466" stroke-width="2"/></svg><h4 style="top:96px">Construction</h4><p style="top:118px">Lorem ipsum is dummy printing text industry.</p></div>
<div class="ind" style="left:498px;top:1845px"><svg class="abs" style="left:64px;top:18px" width="60" height="76" viewBox="0 0 60 76"><polygon points="30,2 58,14 58,44 30,74 2,44 2,14" fill="none" stroke="#0d3466" stroke-width="5"/><circle cx="30" cy="34" r="8" fill="none" stroke="#9c6a00" stroke-width="2"/></svg><h4>Construction</h4><p>Lorem ipsum is dummy printing text industry.</p></div>
<div class="ind" style="left:715px;top:1875px"><svg class="abs" style="left:64px;top:18px" width="60" height="76" viewBox="0 0 60 76"><polygon points="30,2 58,14 58,44 30,74 2,44 2,14" fill="none" stroke="#0d3466" stroke-width="5"/><rect x="21" y="28" width="18" height="14" fill="none" stroke="#9c6a00" stroke-width="2"/></svg><h4>Construction</h4><p>Lorem ipsum is dummy printing text industry.</p></div>
<div class="ind" style="left:935px;top:1822px"><svg class="abs" style="left:64px;top:18px" width="60" height="76" viewBox="0 0 60 76"><polygon points="30,2 58,14 58,44 30,74 2,44 2,14" fill="none" stroke="#0d3466" stroke-width="5"/><polygon points="30,22 40,30 40,44 20,44 20,30" fill="none" stroke="#9c6a00" stroke-width="2"/></svg><h4>Construction</h4><p>Lorem ipsum is dummy printing text industry.</p></div>

<!-- CAREERS -->
<svg class="abs" style="left:0;top:2125px" width="1200" height="395" viewBox="0 0 1200 395">
  <defs><linearGradient id="carPh" x1="0" y1="0" x2="1" y2="0"><stop offset="0" stop-color="#e3e3e3"/><stop offset=".55" stop-color="#bdbdbd"/><stop offset="1" stop-color="#6b6b6b"/></linearGradient></defs>
  <rect y="0" width="1200" height="393" fill="url(#carPh)" role="img" aria-label="Grayscale photo of a guard seen from behind, wearing a cap and a security jacket"/>
  <polygon points="0,0 1200,0 1200,57 0,12" fill="#fff"/>
  <polygon points="0,6 1200,52 1200,60 0,14" fill="#9c6a00"/>
</svg>
<h2 class="abs sec-title" style="left:97px;top:2230px">Careers</h2>
<p class="abs body-text" style="left:60px;top:2294px;width:540px">Ridgeway Patrol is always looking for applicants. We welcome applicants who don't mind being on their feet for long periods of time, don't mind working outside normal business hours and enjoy the challenges presented in the important role of protecting people and property.</p>
<div class="btn" style="left:60px;top:2393px;width:116px;height:37px">Contact Us</div>

<!-- JOIN TEAM -->
<svg class="abs" style="left:90px;top:2585px" width="410" height="400" viewBox="0 0 410 400">
  <polygon points="290,22 406,136 290,250 176,136" fill="#c7cdd6" stroke="#0d3466" stroke-width="5" role="img" aria-label="Photo of an officer in a suit"/>
  <polygon points="165,128 320,283 165,398 40,283" fill="#3b3e44" stroke="#0d3466" stroke-width="5" role="img" aria-label="Photo of a guard in tactical gear"/>
  <polygon points="145,6 300,160 145,310 6,160" fill="#5b5f66" stroke="#9c6a00" stroke-width="6" role="img" aria-label="Photo of a guard with arms folded wearing a cap and security shirt"/>
</svg>
<h2 class="abs sec-title" style="left:600px;top:2615px">Join To Team</h2>
<p class="abs body-text" style="left:600px;top:2680px;width:405px">Ridgeway Patrol is New Brunswick owned and operated.  We are committed to make sure your tools, and hard earned assets don't get stolen.  We are there to make sure your event runs smooth and unwanted situations are prevented and/or taken care of. You have eyes and ears 24/7.  ...We are there.  We're ready, so give us a call.</p>
<div class="btn blue-corner" style="left:600px;top:2833px;width:112px;height:37px">Join Team</div>

<!-- FOOTER -->
<svg class="abs" style="left:0;top:3040px" width="1200" height="410" viewBox="0 0 1200 410">
  <polygon points="0,4 1200,46 1200,410 0,410" fill="#9c6a00"/>
  <polygon points="0,0 1200,40 1200,50 0,12" fill="#0d3466"/>
</svg>
<div class="abs" style="left:706px;top:2860px;width:494px;height:215px;background:linear-gradient(180deg,#f2f2f2,#c9cdd3);border-radius:90px 0 30px 60px" role="img" aria-label="Photo of a white patrol car with blue and gold company livery"></div>

<div class="abs brand" style="left:40px;top:3170px;width:160px"><span class="brand-mark"></span>Ridgeway Patrol</div>

<h3 class="abs foot-h" style="left:336px;top:3163px">Site Map</h3>
<ul class="abs foot-list" style="left:336px;top:3194px">
  <li>Home</li><li>About Us</li><li>Services</li><li>Industries</li><li>Careers</li><li>Contact Us</li>
</ul>
<h3 class="abs foot-h" style="left:612px;top:3163px">Services</h3>
<ul class="abs foot-list" style="left:612px;top:3194px">
  <li>Static Security</li><li>Retail Security</li><li>VIP Security</li><li>Consulting</li><li>Investigation</li><li>Disaster &amp; Crime Scenes</li><li>Labour Disputes</li><li>Support</li>
</ul>
<h3 class="abs foot-h" style="left:888px;top:3163px">Contact Us</h3>
<div class="abs" style="left:888px;top:3198px;display:flex;flex-direction:column;gap:14px">
  <div class="contact-row"><svg width="34" height="34" viewBox="0 0 34 34"><polygon points="17,1 33,9 33,25 17,33 1,25 1,9" fill="#fff"/><path d="M17 9a5 5 0 0 1 5 5c0 4-5 10-5 10s-5-6-5-10a5 5 0 0 1 5-5z" fill="#0d3466"/><circle cx="17" cy="14" r="2" fill="#fff"/></svg><span>240 Harbour Lane,<br>Suite 12 Moncton  NB E1C 4T7</span></div>
  <div class="contact-row"><svg width="34" height="34" viewBox="0 0 34 34"><polygon points="17,1 33,9 33,25 17,33 1,25 1,9" fill="#fff"/><path d="M11 10l4 -1 2 5 -2 2c1 2 3 4 5 5l2-2 5 2-1 4c-8 0-15-7-15-15z" fill="#0d3466"/></svg><span>555.014.2290</span></div>
  <div class="contact-row"><svg width="34" height="34" viewBox="0 0 34 34"><polygon points="17,1 33,9 33,25 17,33 1,25 1,9" fill="#fff"/><rect x="10" y="12" width="14" height="10" fill="#0d3466"/><polyline points="10,12 17,18 24,12" fill="none" stroke="#fff" stroke-width="1.5"/></svg><span>info@ridgewaypatrol.com</span></div>
</div>

<div class="abs copy">Copyright 2022. Ridgeway Patrol-All Right Reserved.</div>

</body>
</html>
```